Postcard Design for Direct Mail Campaign for PIttsburgh area attorney

I am an attorney in Pittsburgh, I did this before and selected three designs. I am not sure if those responding can see which three I selected. Those designs are in use now. All 3 go out. The issue is they cost the standard mailing rate and I will use all 3 of those forever. There will be times I would like to take advantage of the postcard mailing rate and thus this one is smaller. I want the postcard to emphasize I do criminal and SOME civil law. See my sites www.brookvaledefenselaw.com and www.tovacounsel.net.

IN FACT I AM PUTTING THE THREE I AM MAILING RIGHT NOW IN THE IMAGES> I TRUST THAT THESE WILL BE USED TO INSPIRE AND GUIDE AND NO COPY. i Cannot upload those images. You can probably see my 3 winners.

Target Market(s)

Pittsburgh area people who may need a criminal attorney or a civil attorney.

Industry/Entity Type

Legal

Colors
ec1f27

Requirements
Must have
• A balanced criminal - civil thing as these are going to people in the mail with no envelope.
Nice to have
• On my site www.brookvaledefenselaw.com I have badges in the sidebar.
Should not have
• People being arrested. I am putting up new images.

```html
<!DOCTYPE html>
<html lang="en">
<head>
<meta charset="utf-8">
<title>Daniel R. Hartwell Law Office Postcard</title>
<link rel="stylesheet" href="https://fonts.googleapis.com/css2?family=Roboto+Condensed:ital,wght@0,400;0,700;1,700&family=Open+Sans:wght@400;600&family=Cormorant+Garamond:wght@500;600&display=swap">
<style>
  :root {
    --navy: #1d2a57;
    --red: #ec1f27;
    --dark: #262626;
    --gold: #b89a5a;
    --white: #ffffff;
    --ink: #222222;
    --backdrop: #7a5a3c;
    --stamp: #cfcfcf;
  }
  * { margin: 0; padding: 0; box-sizing: border-box; }
  html, body { width: 907px; height: 1200px; overflow: hidden; }
  body { background: var(--backdrop); position: relative; font-family: "Open Sans", sans-serif; }

  .postcard { position: absolute; left: 98px; width: 712px; height: 480px; background: var(--white); overflow: hidden; }
  .postcard--front { top: 98px; }
  .postcard--back { top: 617px; }
  .shapes { position: absolute; inset: 0; }
  .abs { position: absolute; }

  /* Front */
  .brand-kicker { left: 28px; top: 38px; font-family: "Cormorant Garamond", serif; font-weight: 500; font-size: 31px; color: var(--gold); letter-spacing: .5px; }
  .brand-name { left: 28px; top: 74px; font-family: "Roboto Condensed", sans-serif; font-weight: 700; font-size: 25px; color: var(--white); }
  .headline { left: 26px; top: 132px; font-family: "Roboto Condensed", sans-serif; font-weight: 700; font-size: 40px; color: var(--white); }
  .attorney-line { left: 24px; top: 218px; font-family: "Roboto Condensed", sans-serif; font-weight: 700; font-size: 24px; color: var(--white); }

  .services li { position: absolute; list-style: none; font-size: 16px; color: var(--ink); white-space: nowrap; padding-left: 16px; }
  .services li::before { content: ""; position: absolute; left: 2px; top: 3px; width: 5px; height: 10px; border: solid var(--red); border-width: 0 3px 3px 0; transform: rotate(40deg); }

  .contact-line { left: 326px; font-size: 16px; color: var(--white); }
  .contact-line svg { position: absolute; left: -18px; top: 3px; }
  .contact-phone { top: 413px; }
  .contact-web { top: 440px; }

  /* Back */
  .experience { left: 20px; top: 22px; font-family: "Roboto Condensed", sans-serif; font-style: italic; font-weight: 700; font-size: 16.5px; line-height: 19.5px; color: var(--white); }
  .office-card { left: 0; top: 108px; width: 350px; text-align: center; }
  .office-kicker { font-family: "Roboto Condensed", sans-serif; font-weight: 700; font-size: 19px; color: #b0232a; }
  .office-name { margin: 8px auto 0; width: 168px; padding-bottom: 4px; border-bottom: 2px solid var(--navy); font-family: "Cormorant Garamond", serif; font-weight: 600; font-size: 19px; color: var(--gold); white-space: nowrap; }
  .office-cta { margin-top: 7px; font-family: "Roboto Condensed", sans-serif; font-size: 14.5px; color: var(--ink); }
  .office-phone { font-family: "Roboto Condensed", sans-serif; font-weight: 700; font-size: 18px; color: var(--navy); }
  .office-web { margin-top: 4px; font-family: "Roboto Condensed", sans-serif; font-size: 14.5px; line-height: 21px; color: var(--ink); }
  .office-address { left: 18px; top: 292px; width: 170px; font-size: 13px; line-height: 16px; color: var(--white); }
</style>
</head>
<body>

<section class="postcard postcard--front">
  <svg class="shapes" width="712" height="480" viewBox="0 0 712 480">
    <rect x="300" y="0" width="412" height="262" fill="#8a5a2e" role="img" aria-label="Photo of brass scales of justice and a wooden gavel"/>
    <polygon points="0,0 300,0 330,122 0,122" fill="var(--navy)"/>
    <polygon points="298,0 307,0 382,262 373,262" fill="var(--red)"/>
    <polygon points="0,124 350,124 370,194 0,194" fill="var(--red)"/>
    <polygon points="0,200 350,200 368,262 0,262" fill="var(--dark)"/>
    <rect x="370" y="258" width="342" height="4" fill="var(--red)"/>
    <polygon points="0,264 280,264 314,480 0,480" fill="#5a6b82" role="img" aria-label="Photo of a police officer writing a ticket in a patrol car"/>
    <polygon points="280,264 287,264 321,480 314,480" fill="var(--navy)"/>
    <polygon points="287,264 294,264 328,480 321,480" fill="var(--red)"/>
    <polygon points="308,404 712,404 712,480 321,480" fill="var(--dark)"/>
    <rect x="522" y="420" width="62" height="26" rx="2" fill="#1f5aa8"/>
    <circle cx="616" cy="436" r="20" fill="#1d2f6a"/>
    <circle cx="664" cy="436" r="20" fill="#e4e4e4"/>
  </svg>

  <div class="abs brand-kicker">LAW OFFICE OF</div>
  <div class="abs brand-name">DANIEL R. HARTWELL</div>
  <div class="abs headline">Need an attorney?</div>
  <div class="abs attorney-line">ATTORNEY DANIEL R. HARTWELL</div>

  <ul class="services">
    <li style="left:294px;top:278px">Free consultation</li>
    <li style="left:300px;top:304px">Most civil matters</li>
    <li style="left:306px;top:330px">Affordable fees</li>
    <li style="left:312px;top:356px">DUI &amp; traffic citations</li>
    <li style="left:494px;top:282px">Credit cards accepted</li>
    <li style="left:494px;top:308px">License restoration</li>
    <li style="left:494px;top:334px">All criminal matters</li>
  </ul>

  <div class="abs contact-line contact-phone">
    <svg width="13" height="13" viewBox="0 0 13 13"><rect width="13" height="13" rx="2" fill="var(--red)"/><path d="M4 3l1.5 0 .7 2-1 .8c.5 1 1.2 1.7 2.2 2.2l.8-1 2 .7v1.5c-3.5 0-6.2-2.7-6.2-6.2z" fill="var(--white)"/></svg>
    412-555-0148
  </div>
  <div class="abs contact-line contact-web">
    <svg width="12" height="12" viewBox="0 0 12 12"><circle cx="6" cy="6" r="5.5" fill="var(--red)"/><path d="M.5 6h11M6 .5c2 2 2 9 0 11M6 .5c-2 2-2 9 0 11" stroke="var(--dark)" stroke-width=".8" fill="none"/></svg>
    www.tovacounsel.net
  </div>
</section>

<section class="postcard postcard--back">
  <svg class="shapes" width="712" height="480" viewBox="0 0 712 480">
    <polygon points="0,0 390,0 380,100 0,100" fill="var(--dark)"/>
    <polygon points="340,100 354,100 354,275 340,275" fill="var(--white)"/>
    <polygon points="353,100 361,100 356,385 348,385" fill="var(--navy)"/>
    <polygon points="361,100 367,100 362,385 356,385" fill="var(--red)"/>
    <rect x="0" y="275" width="350" height="110" fill="var(--navy)"/>
    <circle cx="216" cy="326" r="28" fill="#1a2b66" stroke="#c9a955" stroke-width="2"/>
    <circle cx="282" cy="326" r="26" fill="#f1f1f1"/>
    <rect x="628" y="16" width="70" height="77" fill="var(--stamp)"/>
    <rect x="20" y="408" width="50" height="52" rx="3" fill="#1d3b78"/>
    <circle cx="105" cy="430" r="24" fill="#2a78c2"/>
    <circle cx="166" cy="430" r="24" fill="#ececec" stroke="#1d3b78" stroke-width="2"/>
    <rect x="198" y="410" width="46" height="40" rx="2" fill="#1d4b9a"/>
    <rect x="250" y="413" width="70" height="18" rx="3" fill="#e2b021"/>
  </svg>

  <div class="abs experience">Over 25 Years of Experience in Criminal Defense<br>DUI Defense and Personal Injury Cases.<br>Serving all of Western PA.</div>

  <div class="abs office-card">
    <div class="office-kicker">LAW OFFICE OF</div>
    <div class="office-name">DANIEL R. HARTWELL</div>
    <div class="office-cta">SCHEDULE AN APPOINTMENT</div>
    <div class="office-phone">412-555-0148</div>
    <div class="office-web">WWW.TOVACOUNSEL.NET<br>WWW.BROOKVALEDEFENSELAW.COM</div>
  </div>

  <div class="abs office-address">The Law Office of Daniel R. Hartwell 610 Alder Building 52 Linden Avenue Pittsburgh, PA 15219</div>
</section>

</body>
</html>
```